BrookhavenLLC

Real Estate Investment. Buy/Sell house/investment . Trustworthy,Reliable, and friendly

Industry/Entity Type

Real Estate

Contact Information for Business Card

Brookhaven@mailbox-example.com
808-555-0143
Linnea-Joy Patterson

```html
<!DOCTYPE html>
<html lang="en">
<head>
<meta charset="UTF-8">
<title>Brookhaven LLC – Business Card</title>
<link href="https://fonts.googleapis.com/css2?family=Oswald:wght@500&family=Quicksand:wght@400&display=swap" rel="stylesheet">
<style>
  :root {
    --page-bg: #2b2b2b;
    --card-blue: #0f70b0;
    --card-ink: #e4e4e4;
    --rule: #e8e8e8;
  }
  * { margin: 0; padding: 0; box-sizing: border-box; }
  html, body {
    width: 1200px;
    height: 800px;
    overflow: hidden;
    background: var(--page-bg);
  }
  .canvas {
    position: relative;
    width: 1200px;
    height: 800px;
    display: flex;
    align-items: center;
    justify-content: center;
  }
  .business-card {
    position: relative;
    width: 1050px;
    height: 600px;
    background: var(--card-blue);
    border-radius: 44px;
    color: var(--card-ink);
    overflow: hidden;
  }
  .company-name {
    position: absolute;
    left: 0;
    right: 0;
    top: 150px;
    text-align: center;
    font-family: "Oswald", sans-serif;
    font-weight: 500;
    font-size: 54px;
    letter-spacing: 3px;
    text-transform: uppercase;
  }
  .person-name {
    position: absolute;
    right: 70px;
    top: 262px;
    font-family: "Oswald", sans-serif;
    font-weight: 500;
    font-size: 36px;
    letter-spacing: 3px;
    text-transform: uppercase;
  }
  .divider {
    position: absolute;
    left: 0;
    right: 0;
    top: 330px;
    height: 5px;
    background: var(--rule);
  }
  .contact-list {
    position: absolute;
    left: 80px;
    top: 385px;
    list-style: none;
    font-family: "Quicksand", sans-serif;
    font-weight: 400;
  }
  .contact-item {
    display: flex;
    align-items: center;
    gap: 26px;
    height: 58px;
    margin-bottom: 22px;
    font-size: 34px;
    letter-spacing: 3px;
  }
  .contact-item.email { font-size: 32px; letter-spacing: 1px; padding-left: 22px; }
  .contact-icon { width: 52px; height: 52px; flex: none; }
</style>
</head>
<body>
<main class="canvas">
  <section class="business-card" aria-label="Brookhaven LLC business card">
    <h1 class="company-name">Brookhaven LLC</h1>
    <p class="person-name">Linnea-Joy Patterson</p>
    <div class="divider"></div>
    <ul class="contact-list">
      <li class="contact-item phone">
        <svg class="contact-icon" viewBox="0 0 52 52" aria-hidden="true">
          <polygon points="26,3 49,20 40,48 12,48 3,20" fill="var(--card-ink)"/>
          <path d="M19 17c2-2 4-1 5 1l1 3c0 1-1 2-2 3 1 3 3 5 6 6 1-1 2-2 3-2l3 1c2 1 2 3 1 5-2 2-5 2-8 1-5-2-9-6-11-11-1-3-0-5 2-7z" fill="var(--card-blue)"/>
        </svg>
        <span>808-555-0143</span>
      </li>
      <li class="contact-item email">
        <svg class="contact-icon" viewBox="0 0 52 52" aria-hidden="true">
          <polygon points="26,3 49,20 40,48 12,48 3,20" fill="var(--card-ink)"/>
          <rect x="13" y="18" width="26" height="17" fill="none" stroke="var(--card-blue)" stroke-width="2.5"/>
          <polyline points="13,18 26,29 39,18" fill="none" stroke="var(--card-blue)" stroke-width="2.5"/>
        </svg>
        <span>Brookhaven@mailbox-example.com</span>
      </li>
    </ul>
  </section>
</main>
</body>
</html>
```